Acai Bowl and Coffee Van need new Menus

We currently have a basic menu that is displayed in an A3 frame. It lacks images, specifically of the Acai Bowls and is difficult to read and understand.

We need a new Acai Bowl Menu and a new Drink Menu but in a more attractive and easier to read format.
We would like images of the Acai Bowls (using Images supplied or make your own) in order to show customers what is on each bowl. Customers chose what granola they would like from the three that are available. Currently we tell customers to check the bottom of the menu as they are often unaware they get to chose.

The drink menu items are simple (we have removed smoothies from our menu entirely).
The drink menu needs to have "Chai Latte" and "Dirty Chai Latte" added as options with the same S,M,L pricing as a Latte.

I have attached images of the menus and a photo of how the menus are displayed on The Moro Cart. Also attached is photos of the Acai Bowls and other food / drink items on the menu if you wish to use them in your design. I have included the files for all of our logo variations.

Our main objective with the menu redesign is to have the menu more appealing and easier to read and understand.

Industry/Entity Type

Food and Coffee

Font styles to use
Other font styles liked:
• Orplid Pro (Fill and Shadow), Trend Sans One

Colors

Designer to choose colors to be used in the design.

Requirements
Must have
• The final design must include prices and be editable in the case of any price changes in the future.

```html
<!DOCTYPE html>
<html lang="en">
<head>
<meta charset="utf-8">
<title>The Moro Cart – Menus</title>
<link rel="stylesheet" href="https://fonts.googleapis.com/css2?family=Josefin+Sans:wght@700&family=Montserrat:wght@500;600&display=swap">
<style>
:root{
  --backdrop:#eeeded;
  --sage:#d9e1d7;
  --blush:#eedfe2;
  --mocha:#9c8265;
  --tan:#a4875e;
  --ink:#1d1d1d;
  --cream:#f8f5ef;
  --white:#ffffff;
}
html,body{margin:0;padding:0;width:1200px;height:1200px;overflow:hidden;background:var(--backdrop);}
.stage{position:relative;width:1932px;height:1932px;transform:scale(0.621118);transform-origin:0 0;font-family:"Montserrat",sans-serif;color:var(--ink);}
.sheet{position:absolute;}
.sheet--drinks{left:71px;top:357px;width:860px;height:1214px;background:var(--sage);}
.sheet--bowls{left:997px;top:357px;width:859px;height:1217px;background:var(--blush);}
.t{position:absolute;line-height:1;white-space:nowrap;}
.title{font-family:"Josefin Sans",sans-serif;font-weight:700;font-size:140px;letter-spacing:0;color:var(--cream);transform:scaleX(0.86);transform-origin:0 0;
  text-shadow:
    2px 0 0 var(--mocha),-2px 0 0 var(--mocha),0 2px 0 var(--mocha),0 -2px 0 var(--mocha),
    1.5px 1.5px 0 var(--mocha),-1.5px 1.5px 0 var(--mocha),1.5px -1.5px 0 var(--mocha),-1.5px -1.5px 0 var(--mocha),
    3px 3px 0 var(--mocha),4px 4px 0 var(--mocha),5px 5px 0 var(--mocha),6px 6px 0 var(--mocha),7px 7px 0 var(--mocha);}
.heading{font-size:20px;font-weight:600;letter-spacing:.13em;}
.col-label{font-size:11.5px;font-weight:500;letter-spacing:.12em;color:var(--tan);}
.item{font-size:13px;font-weight:600;letter-spacing:.09em;}
.note{font-size:10.5px;font-weight:500;letter-spacing:.08em;color:var(--tan);}
.price{position:absolute;height:18px;width:58px;background:var(--white);border-radius:3px;font-size:13.5px;font-weight:600;letter-spacing:.08em;line-height:19px;text-align:center;}
.price--wide{width:67px;}
.badge{position:absolute;border-radius:50%;background:var(--white);}
.step{position:absolute;width:54px;height:54px;border-radius:50%;background:var(--tan);color:var(--cream);font-family:"Josefin Sans",sans-serif;font-weight:700;font-size:38px;line-height:62px;text-align:center;}
.frame{position:absolute;border:2px solid var(--white);border-radius:12px;}
.bowl-name{font-size:20px;font-weight:600;letter-spacing:.12em;}
.bowl-desc{font-size:12.5px;font-weight:600;letter-spacing:.09em;}
.bowl-price{position:absolute;height:18px;width:64px;background:var(--white);border-radius:3px;font-size:12.5px;font-weight:600;letter-spacing:.06em;line-height:19px;text-align:center;}
.topping-list{position:absolute;margin:0;padding:0;list-style:none;font-size:11.5px;font-weight:600;letter-spacing:.08em;line-height:15.6px;}
.topping-list li::before{content:"• ";}
.topping-list li.cont::before{content:"\00a0\00a0";}
.pill{display:inline-block;background:var(--tan);color:var(--white);font-size:6.5px;letter-spacing:.06em;padding:1px 5px;border-radius:6px;margin:1px 0;}
.brand{position:absolute;display:flex;align-items:center;gap:14px;}
.brand__dot{width:22px;height:22px;border-radius:50%;background:var(--tan);}
.brand__name{font-size:24px;font-weight:600;letter-spacing:.2em;color:var(--mocha);}
</style>
</head>
<body>
<div class="stage">

  <section class="sheet sheet--drinks" aria-label="Drinks menu"></section>
  <h1 class="t title" style="left:126px;top:412px;margin:0;">DRINKS</h1>
  <div class="t title" style="left:126px;top:536px;">MENU</div>

  <div class="t heading" style="left:129px;top:697px;">COFFEE</div>
  <div class="t col-label" style="left:316px;top:704px;">SMALL</div>
  <div class="t col-label" style="left:389px;top:704px;">REG</div>
  <div class="t col-label" style="left:463px;top:704px;">LARGE</div>

  <div class="t item" style="left:128px;top:743px;">CAPPUCCINO</div>
  <div class="price" style="left:305px;top:741px;">5.50</div><div class="price" style="left:379px;top:741px;">6.50</div><div class="price" style="left:452px;top:741px;">7.50</div>
  <div class="t item" style="left:128px;top:763px;">LATTE</div>
  <div class="price" style="left:305px;top:761px;">5.50</div><div class="price" style="left:379px;top:761px;">6.50</div><div class="price" style="left:452px;top:761px;">7.50</div>
  <div class="t item" style="left:128px;top:783px;">FLAT WHITE</div>
  <div class="price" style="left:305px;top:781px;">5.50</div><div class="price" style="left:379px;top:781px;">6.50</div><div class="price" style="left:452px;top:781px;">7.50</div>
  <div class="t item" style="left:128px;top:804px;">ESPRESSO</div>
  <div class="price" style="left:305px;top:802px;">4.00</div><div class="price" style="left:379px;top:802px;">4.50</div><div class="price" style="left:452px;top:802px;">5.00</div>
  <div class="t item" style="left:128px;top:824px;">LONG BLACK</div>
  <div class="price" style="left:305px;top:822px;">4.50</div><div class="price" style="left:379px;top:822px;">5.00</div><div class="price" style="left:452px;top:822px;">5.50</div>
  <div class="t item" style="left:128px;top:844px;">MACCHIATO</div>
  <div class="price" style="left:379px;top:842px;">5.50</div><div class="price" style="left:452px;top:842px;">6.00</div>

  <div class="t heading" style="left:129px;top:908px;">CHOCOLATE</div>
  <div class="t col-label" style="left:316px;top:915px;">SMALL</div>
  <div class="t col-label" style="left:389px;top:915px;">REG.</div>
  <div class="t col-label" style="left:463px;top:915px;">LARGE</div>
  <div class="t item" style="left:128px;top:954px;">MOCHA</div>
  <div class="price" style="left:305px;top:952px;">5.50</div><div class="price" style="left:379px;top:952px;">6.50</div><div class="price" style="left:452px;top:952px;">7.50</div>
  <div class="t item" style="left:128px;top:974px;">HOT CHOCOLATE</div>
  <div class="price" style="left:305px;top:972px;">5.00</div><div class="price" style="left:379px;top:972px;">6.00</div><div class="price" style="left:452px;top:972px;">7.00</div>

  <div class="t heading" style="left:129px;top:1037px;">CHAI LATTE</div>
  <div class="t col-label" style="left:316px;top:1044px;">SMALL</div>
  <div class="t col-label" style="left:389px;top:1044px;">REG.</div>
  <div class="t col-label" style="left:463px;top:1044px;">LARGE</div>
  <div class="t item" style="left:128px;top:1083px;">CHAI LATTE</div>
  <div class="price" style="left:305px;top:1081px;">5.50</div><div class="price" style="left:379px;top:1081px;">6.50</div><div class="price" style="left:452px;top:1081px;">7.50</div>
  <div class="t item" style="left:128px;top:1103px;">DIRTY CHAI LATTE</div>
  <div class="price" style="left:305px;top:1101px;">5.50</div><div class="price" style="left:379px;top:1101px;">6.50</div><div class="price" style="left:452px;top:1101px;">7.50</div>

  <div class="t heading" style="left:129px;top:1164px;">COLD BEVERAGES</div>
  <div class="t col-label" style="left:389px;top:1171px;">REG.</div>
  <div class="t col-label" style="left:463px;top:1171px;">LARGE</div>
  <div class="t item" style="left:128px;top:1210px;">COLD BREW COFFEE</div>
  <div class="price" style="left:379px;top:1208px;">6.50</div><div class="price" style="left:452px;top:1208px;">8.50</div>
  <div class="t item" style="left:128px;top:1230px;">ICED COFFEE</div>
  <div class="price" style="left:379px;top:1228px;">6.50</div><div class="price" style="left:452px;top:1228px;">7.50</div>
  <div class="t item" style="left:128px;top:1251px;">ICED MOCHA</div>
  <div class="price" style="left:379px;top:1249px;">6.50</div><div class="price" style="left:452px;top:1249px;">7.50</div>
  <div class="t item" style="left:128px;top:1271px;">ICED LONG BLACK</div>
  <div class="price" style="left:379px;top:1269px;">5.50</div><div class="price" style="left:452px;top:1269px;">6.50</div>
  <div class="t item" style="left:128px;top:1291px;">ICED CHOCOLATE</div>
  <div class="price" style="left:379px;top:1289px;">6.50</div><div class="price" style="left:452px;top:1289px;">7.50</div>
  <div class="t item" style="left:128px;top:1311px;">ICED LEAF TEA</div>
  <div class="price" style="left:379px;top:1309px;">5.00</div><div class="price" style="left:452px;top:1309px;">6.00</div>
  <div class="t note" style="left:128px;top:1328px;">LEMONGRASS AND GINGER |</div>
  <div class="t note" style="left:128px;top:1343px;">WHITE TEA, ACAI AND COCONUT | CHAI</div>

  <div class="t heading" style="left:129px;top:1404px;">MORE BEVERAGES</div>
  <div class="t item" style="left:128px;top:1450px;">TONIC KOMBUCHA</div>
  <div class="price" style="left:307px;top:1448px;">4.50</div>
  <div class="t item" style="left:128px;top:1470px;">BOTTLED WATER</div>
  <div class="price" style="left:307px;top:1468px;">3.00</div>

  <div class="t heading" style="left:593px;top:695px;">EXTRAS</div>
  <div class="t item" style="left:593px;top:741px;">ADDITIONAL SHOT</div>
  <div class="price" style="left:801px;top:739px;">0.50</div>
  <div class="t item" style="left:593px;top:761px;">SHOT OF SYRUP</div>
  <div class="price" style="left:801px;top:759px;">0.50</div>
  <div class="t note" style="left:592px;top:778px;">VANILLA | CARAMEL | HAZELNUT</div>

  <div class="t heading" style="left:594px;top:907px;">ALTERNATIVE MILKS</div>
  <div class="t item" style="left:593px;top:952px;">OAT MILK</div>
  <div class="price price--wide" style="left:808px;top:950px;">+ 0.70</div>
  <div class="t note" style="left:593px;top:969px;">GREENFIELD DAIRY CO</div>
  <div class="t item" style="left:593px;top:991px;">ALMOND MILK</div>
  <div class="price price--wide" style="left:808px;top:989px;">+ 0.70</div>
  <div class="t note" style="left:593px;top:1008px;">CREAMERY LAB</div>
  <div class="t item" style="left:593px;top:1029px;">SOY MILK</div>
  <div class="price price--wide" style="left:808px;top:1027px;">+ 0.70</div>
  <div class="t note" style="left:593px;top:1046px;">SUNNY SOY CO</div>
  <div class="t item" style="left:593px;top:1067px;">LACTOSE FREE</div>
  <div class="price price--wide" style="left:808px;top:1065px;">+ 0.70</div>
  <div class="t note" style="left:593px;top:1084px;">CREAMERY LAB</div>

  <div class="badge" style="left:687px;top:1123px;width:140px;height:140px;"></div>
  <div class="t" style="left:700px;top:1156px;width:114px;text-align:center;transform:rotate(10deg);color:var(--tan);font-weight:600;line-height:1.05;white-space:normal;">
    <div style="font-size:9px;letter-spacing:.1em;">SAVE</div>
    <div style="font-size:14px;letter-spacing:.1em;">50 CENTS</div>
    <div style="font-size:8px;letter-spacing:.1em;">WITH YOUR OWN</div>
    <div style="font-size:14px;letter-spacing:.1em;">REUSABLE<br>CUP</div>
  </div>

  <div class="t heading" style="left:594px;top:1321px;">LEAF TEA</div>
  <div class="t col-label" style="left:812px;top:1328px;">REG.</div>
  <div class="t item" style="left:594px;top:1367px;">ENGLISH BREAKFAST</div><div class="price" style="left:803px;top:1365px;">4.00</div>
  <div class="t item" style="left:594px;top:1387px;">MORNING DEW</div><div class="price" style="left:803px;top:1385px;">4.00</div>
  <div class="t item" style="left:594px;top:1408px;">GUNPOWDER GREEN</div><div class="price" style="left:803px;top:1406px;">4.00</div>
  <div class="t item" style="left:594px;top:1428px;">CHAI TEA</div><div class="price" style="left:803px;top:1426px;">4.00</div>
  <div class="t item" style="left:594px;top:1448px;">PEPPERMINT</div><div class="price" style="left:803px;top:1446px;">4.00</div>
  <div class="t item" style="left:594px;top:1468px;">COCOA &amp; PEPPERMINT</div><div class="price" style="left:803px;top:1466px;">4.00</div>

  <section class="sheet sheet--bowls" aria-label="Acai bowls menu"></section>
  <h2 class="t title" style="left:1045px;top:412px;margin:0;">AÇAI</h2>
  <div class="t title" style="left:1045px;top:536px;">BÓWLS</div>

  <div class="step" style="left:1033px;top:685px;">1</div>
  <div class="t heading" style="left:1104px;top:693px;">AÇAI BASE</div>

  <div class="step" style="left:1321px;top:685px;">2</div>
  <div class="t heading" style="left:1392px;top:694px;">PICK YOUR ♥-GRANOLA</div>
  <div class="frame" style="left:1348px;top:720px;width:469px;height:199px;"></div>
  <div class="t item" style="left:1370px;top:731px;">GINGERNUT CRUNCH</div>
  <div class="t note" style="left:1370px;top:749px;line-height:14.5px;">INSPIRED BY BELOVED GINGER NUT BISCUITS, THIS GRANOLA<br>BRINGS THE WARMTH AND COMFORT OF GINGER, NUTMEG, AND<br>CINNAMON TO YOUR FAVOURITE BOWL.</div>
  <div class="t item" style="left:1370px;top:807px;">TOASTED ALMOND &amp; CINNAMON</div>
  <div class="t note" style="left:1370px;top:825px;line-height:14.5px;">COMBINES THE WARMTH OF CINNAMON WITH TOASTED<br>AUSSIE ALMONDS AND 100% WA GROWN LUPIN FLAKES.</div>
  <div class="t item" style="left:1370px;top:869px;">CACAO, HAZELNUT &amp; CHIA</div>
  <div class="t note" style="left:1370px;top:886px;line-height:14.5px;">ONE FOR THE CHOCOLATE LOVERS, TASTES LIKE A<br>CRUNCHY CHOC SPREAD WITH HAZELNUTS AND CACAO.</div>

  <div class="badge" style="left:1141px;top:775px;width:140px;height:140px;"></div>
  <div class="t" style="left:1154px;top:800px;width:114px;text-align:center;transform:rotate(12deg);color:var(--tan);font-weight:600;line-height:1.1;white-space:normal;">
    <div style="font-size:9.5px;letter-spacing:.08em;">WE USE BAYSIDE<br>CRUNCH GRANOLA:</div>
    <span class="pill">VEGAN FRIENDLY</span><br><span class="pill">NO REFINED SUGARS</span><br><span class="pill">DAIRY FREE</span><br><span class="pill">GLUTEN FREE</span>
  </div>
  <svg style="position:absolute;left:1264px;top:850px;" width="76" height="45" viewBox="0 0 76 45" aria-hidden="true">
    <path d="M4 40 Q40 38 68 10" fill="none" stroke="#fff" stroke-width="2" stroke-dasharray="3 3"/>
    <path d="M60 10 L71 5 L68 17 Z" fill="#fff"/>
  </svg>

  <div class="step" style="left:1030px;top:925px;">3</div>
  <div class="t heading" style="left:1101px;top:937px;">PICK YOUR ♥-TOPPING COMBO</div>
  <div class="frame" style="left:1060px;top:963px;width:756px;height:397px;"></div>
  <svg style="position:absolute;left:1060px;top:963px;" width="760" height="400" aria-hidden="true">
    <line x1="372" y1="14" x2="372" y2="385" stroke="#fff" stroke-width="1.5" stroke-dasharray="2 4"/>
    <line x1="12" y1="127" x2="745" y2="127" stroke="#fff" stroke-width="1.5" stroke-dasharray="2 4"/>
    <line x1="12" y1="259" x2="745" y2="259" stroke="#fff" stroke-width="1.5" stroke-dasharray="2 4"/>
  </svg>

  <div class="t bowl-name" style="left:1088px;top:976px;">ORIGINAL BOWL</div>
  <div class="bowl-price" style="left:1335px;top:976px;">$ 17.50</div>
  <div class="t bowl-desc" style="left:1088px;top:1012px;line-height:17.5px;">COCONUT FLAKES AND FRESH<br>SEASONAL FRUIT</div>
  <div class="t note" style="left:1088px;top:1049px;line-height:15px;">A BASIC BOWL, GREAT FOR YOU TO<br>START YOUR OWN CREATION</div>

  <div class="t bowl-name" style="left:1462px;top:976px;">TROPICAL BOWL</div>
  <div class="bowl-price" style="left:1717px;top:976px;">$ 18.50</div>
  <div class="t bowl-desc" style="left:1462px;top:1012px;line-height:17.5px;">SHREDDED COCONUT, PASSIONFRUIT,<br>MANGO AND PINEAPPLE</div>
  <div class="t note" style="left:1462px;top:1049px;line-height:15px;">MAKE IT EXTRA REFRESHING BY ADDING<br>SOME KIWIFRUIT FOR $1.00</div>

  <div class="t bowl-name" style="left:1088px;top:1105px;">BERRY BOWL</div>
  <div class="bowl-price" style="left:1335px;top:1104px;">$ 18.50</div>
  <div class="t bowl-desc" style="left:1088px;top:1141px;line-height:17.5px;">SHREDDED COCONUT. GOJI BERRIES.<br>STRAWBERRY AND BLUEBERRY</div>
  <div class="t note" style="left:1088px;top:1178px;line-height:15px;">ADD SOME CACAO NIBS FOR AN<br>EXTRA $1.00</div>

  <div class="t bowl-name" style="left:1462px;top:1105px;">CHOC BOWL</div>
  <div class="bowl-price" style="left:1721px;top:1105px;">$20.50</div>
  <div class="t bowl-desc" style="left:1462px;top:1141px;line-height:17.5px;">SHREDDED COCONUT, CACAO NIBS,<br>BANANA, STRAWBERRY AND CHOC SPREAD</div>
  <div class="t note" style="left:1462px;top:1178px;line-height:15px;">WE RECOMMEND THE ‚CACAO, HAZELNUT<br>&amp; CHIA GRANOLA' WITH THIS ONE</div>

  <div class="t bowl-name" style="left:1088px;top:1235px;">COOKIE BOWL</div>
  <div class="bowl-price" style="left:1335px;top:1235px;">$ 21.00</div>
  <div class="t bowl-desc" style="left:1088px;top:1272px;line-height:18px;">BANANA,SHREDDED COCONUT,<br>GOJI BERRIES, COOKIE SPREAD<br>AND CRUMBLE</div>
  <div class="t note" style="left:1088px;top:1327px;line-height:15px;">IF YOU LOVE PEANUT BUTTER, YOU<br>WILL LOVE THIS BOWL TOO</div>

  <div class="t bowl-name" style="left:1462px;top:1235px;">MORO FAVOURITE</div>
  <div class="bowl-price" style="left:1717px;top:1235px;">$ 21.00</div>
  <div class="t bowl-desc" style="left:1462px;top:1272px;line-height:17.5px;">COCONUT FLAKES, GOJI BERIES,<br>CHIA SEEDS, BANANA, STRAWBERRY<br>AND PEANUT BUTTER</div>
  <div class="t note" style="left:1462px;top:1327px;line-height:15px;">ADD A PEANUT BUTTER PROTEIN SLICE<br>ON TOP FOR $ 2.50</div>

  <div class="step" style="left:1033px;top:1371px;">4</div>
  <div class="t heading" style="left:1104px;top:1381px;">ADDITIONAL TOPPINGS</div>
  <div class="frame" style="left:1060px;top:1408px;width:756px;height:117px;"></div>
  <svg style="position:absolute;left:1060px;top:1408px;" width="760" height="120" aria-hidden="true">
    <line x1="212" y1="10" x2="212" y2="110" stroke="#fff" stroke-width="1.5" stroke-dasharray="2 4"/>
    <line x1="387" y1="10" x2="387" y2="110" stroke="#fff" stroke-width="1.5" stroke-dasharray="2 4"/>
    <line x1="576" y1="10" x2="576" y2="110" stroke="#fff" stroke-width="1.5" stroke-dasharray="2 4"/>
  </svg>
  <ul class="topping-list" style="left:1085px;top:1420px;">
    <li>CHIA SEEDS</li><li>PASSIONFRUIT</li><li>BUCKWHEAT MIX</li><li>COCONUT FLAKES</li><li>SHREDDED COCONUT</li>
  </ul>
  <ul class="topping-list" style="left:1288px;top:1420px;">
    <li>GOJI BERRIES</li><li>CACAO NIBS</li><li>HONEY</li><li>DATES</li><li>EXTRA FRUIT</li><li>EXTRA GRANOLA</li>
  </ul>
  <ul class="topping-list" style="left:1465px;top:1420px;">
    <li>PEANUT BUTTER</li><li>ALMOND BUTTER</li><li>CHOC SPREAD</li><li>COOKIE SPREAD</li>
  </ul>
  <ul class="topping-list" style="left:1651px;top:1420px;">
    <li>BAYSIDE CRUNCH</li><li class="cont">PEANUT BUTTER</li><li class="cont">PROTEIN SLICE</li>
  </ul>
  <div class="bowl-price" style="left:1132px;top:1522px;width:60px;">$ 0.50</div>
  <div class="bowl-price" style="left:1326px;top:1522px;width:60px;">$ 1.00</div>
  <div class="bowl-price" style="left:1515px;top:1522px;width:60px;">$ 2.00</div>
  <div class="bowl-price" style="left:1696px;top:1522px;width:60px;">$ 2.50</div>

  <div class="brand" style="left:812px;top:1744px;">
    <span class="brand__dot"></span>
    <span class="brand__name">THE MORO CART</span>
  </div>

</div>
</body>
</html>
```